" Trata-se de uma construtora em conjunto com um escritório de engenharia e arquitetura para prestar serviços de construção, gerenciamento de obras e projetos e desenho. "

```html
<!DOCTYPE html>
<html lang="pt-BR">
<head>
<meta charset="UTF-8">
<title>Vértice — Construindo Sonhos</title>
<link href="https://fonts.googleapis.com/css2?family=Montserrat:wght@500;600;700;800&display=swap" rel="stylesheet">
<style>
  :root {
    --canvas-bg: #ececec;
    --sidebar-bg: #3a3d43;
    --gold: #f0ad2e;
    --gold-soft: #d9a445;
    --white: #ffffff;
    --menu-text: #e4e4e4;
    --sky-top: #f6c24f;
    --sky-mid: #d7812e;
    --city-low: #6a5245;
    --city-dark: #2f3036;
  }
  * { margin: 0; padding: 0; box-sizing: border-box; }
  html, body {
    width: 1200px;
    height: 1200px;
    overflow: hidden;
    background: var(--canvas-bg);
    font-family: 'Montserrat', sans-serif;
  }
  .site {
    position: absolute;
    left: 0;
    top: 250px;
    width: 1200px;
    height: 700px;
    display: flex;
  }
  .sidebar {
    width: 260px;
    height: 100%;
    background: var(--sidebar-bg);
    padding: 70px 0 0 40px;
    position: relative;
  }
  .brand {
    display: flex;
    align-items: center;
    gap: 12px;
  }
  .brand-dot {
    width: 14px;
    height: 14px;
    border-radius: 50%;
    background: var(--gold-soft);
  }
  .brand-name {
    color: var(--gold-soft);
    font-weight: 600;
    font-size: 26px;
    letter-spacing: 4px;
  }
  .main-nav {
    margin-top: 150px;
    list-style: none;
  }
  .main-nav li {
    color: var(--menu-text);
    font-weight: 600;
    font-size: 15px;
    letter-spacing: 1.5px;
    line-height: 32px;
  }
  .main-nav li.is-active { color: var(--gold); }
  .social-links {
    display: flex;
    gap: 12px;
    margin-top: 80px;
  }
  .social-links span {
    width: 14px;
    height: 14px;
    border-radius: 50%;
    background: var(--gold);
  }
  .hero {
    position: relative;
    flex: 1;
    height: 100%;
    overflow: hidden;
  }
  .hero-photo {
    position: absolute;
    inset: 0;
    background: linear-gradient(180deg, var(--sky-top) 0%, var(--sky-mid) 30%, var(--city-low) 62%, var(--city-dark) 100%);
  }
  .hero-title {
    position: absolute;
    left: 70px;
    top: 230px;
    color: var(--white);
    font-weight: 700;
    font-size: 50px;
    line-height: 64px;
    letter-spacing: -0.5px;
  }
  .hero-title .highlight { color: var(--gold); }
  .scroll-down {
    position: absolute;
    left: 340px;
    top: 460px;
    width: 64px;
    height: 64px;
  }
</style>
</head>
<body>
  <div class="site">
    <aside class="sidebar">
      <div class="brand">
        <span class="brand-dot"></span>
        <span class="brand-name">Vértice</span>
      </div>
      <ul class="main-nav">
        <li class="is-active">HOME</li>
        <li>QUEM SOMOS</li>
        <li>SERVIÇOS</li>
        <li>DEPOIMENTOS</li>
        <li>FALE CONOSCO</li>
      </ul>
      <div class="social-links">
        <span></span><span></span><span></span>
      </div>
    </aside>
    <section class="hero">
      <div class="hero-photo" role="img" aria-label="Foto de arranha-céus de uma grande cidade ao pôr do sol com céu dourado"></div>
      <h1 class="hero-title">Construindo <span class="highlight">Sonhos</span><br>Administrando o futuro.</h1>
      <svg class="scroll-down" viewBox="0 0 64 64" aria-label="Rolar para baixo">
        <circle cx="32" cy="32" r="30" fill="#ffffff"/>
        <path d="M32 18 V44 M21 34 L32 45 L43 34" fill="none" stroke="#3a3d43" stroke-width="4" stroke-linecap="round" stroke-linejoin="round"/>
      </svg>
    </section>
  </div>
</body>
</html>
```